Relocation/furniture installation company needs new business cards

we are a relocation and furniture installation company mainly dealing with corporate clients and we are looking for new business card ideas. Cards should incorporate our logo and list our website, phone number and services. The company is only 2 years old but with more staff joining we are in the need for more business cards, so something with an awesome design that is eye catching would go a long way to insure we get our name out there and look good to potential new clients.

Target Market(s)

Corporate

Industry/Entity Type

Trade

Contact Information for Business Card

www.merovanta.co.nz
0508 7 kelpor

furniture installation
business relocations
joinery installation
commercial property maintenance

Colors
0592cd
34a7d8
85cae6
85acd3
0356a4
cfdfed
cee9f5
757575
474747

Requirements
Must have
• Business relocations and furniture installation specialists
Nice to have
• something that incorporates our logo.

```html
<!DOCTYPE html>
<html lang="en">
<head>
<meta charset="utf-8">
<title>Merovanta Business Card</title>
<link rel="stylesheet" href="https://fonts.googleapis.com/css2?family=Lato:wght@400;700;900&display=swap">
<style>
  :root {
    --navy: #2e3f8b;
    --sky: #2ea3dc;
    --rule: #4fb3e2;
    --ink: #1a1a1a;
    --muted: #474747;
    --paper: #ffffff;
  }
  * { margin: 0; padding: 0; box-sizing: border-box; }
  html, body { width: 1200px; height: 894px; overflow: hidden; background: var(--paper); }
  .card {
    position: relative;
    width: 1200px;
    height: 894px;
    background: var(--paper);
    font-family: "Lato", sans-serif;
    color: var(--ink);
    overflow: hidden;
  }
  .services {
    position: absolute;
    left: 124px;
    top: 330px;
    display: flex;
    gap: 14px;
    list-style: none;
    font-size: 19px;
    color: var(--muted);
  }
  .services li + li::before {
    content: "";
    display: inline-block;
    width: 6px;
    height: 6px;
    margin-right: 14px;
    vertical-align: middle;
    background: var(--sky);
  }
  .tagline {
    position: absolute;
    left: 124px;
    top: 378px;
    font-weight: 700;
    font-size: 24px;
    color: var(--sky);
  }
  .brand-name {
    position: absolute;
    left: 124px;
    top: 452px;
    display: flex;
    align-items: center;
    gap: 16px;
    font-weight: 900;
    font-size: 64px;
    letter-spacing: 12px;
    color: var(--navy);
    line-height: 1;
  }
  .brand-mark {
    width: 22px;
    height: 22px;
    background: var(--sky);
  }
  .person {
    position: absolute;
    right: 106px;
    top: 520px;
    text-align: right;
  }
  .person-name {
    font-weight: 700;
    font-size: 43px;
    color: var(--sky);
    line-height: 1.1;
  }
  .person-title {
    font-size: 29px;
    color: var(--ink);
    margin-top: 4px;
  }
  .divider {
    position: absolute;
    left: 122px;
    top: 616px;
    width: 972px;
    height: 2px;
    background: var(--rule);
  }
  .contact-list {
    position: absolute;
    left: 124px;
    top: 672px;
    list-style: none;
    font-size: 28px;
  }
  .contact-list li {
    display: flex;
    align-items: center;
    gap: 20px;
    height: 37px;
  }
  .contact-icon { width: 24px; height: 24px; flex: none; }
  .address {
    position: absolute;
    right: 106px;
    top: 706px;
    font-size: 28px;
  }
  .waves { position: absolute; inset: 0; }
  .website {
    position: absolute;
    right: 106px;
    top: 796px;
    font-size: 29px;
    letter-spacing: 1px;
    color: var(--paper);
  }
</style>
</head>
<body>
  <div class="card">
    <ul class="services">
      <li>Furniture installation</li>
      <li>Business relocations</li>
      <li>Joinery installation</li>
      <li>Commercial property maintenance</li>
    </ul>
    <div class="tagline">Business relocations and furniture installation specialists</div>

    <div class="brand-name"><span>MEROVANTA</span><span class="brand-mark"></span></div>

    <div class="person">
      <div class="person-name">Daniel Orrow</div>
      <div class="person-title">Managing Director</div>
    </div>

    <div class="divider"></div>

    <ul class="contact-list">
      <li>
        <svg class="contact-icon" viewBox="0 0 24 24" aria-hidden="true">
          <path fill="#2ea3dc" d="M6.6 10.8c1.4 2.8 3.8 5.1 6.6 6.6l2.2-2.2c.3-.3.7-.4 1-.2 1.1.4 2.3.6 3.6.6.6 0 1 .4 1 1V20c0 .6-.4 1-1 1C10.6 21 3 13.4 3 4c0-.6.4-1 1-1h3.5c.6 0 1 .4 1 1 0 1.3.2 2.5.6 3.6.1.3 0 .7-.2 1l-2.3 2.2z"/>
        </svg>
        <span>0508 7 kelpor</span>
      </li>
      <li>
        <svg class="contact-icon" viewBox="0 0 24 24" aria-hidden="true">
          <rect x="2" y="5" width="20" height="14" fill="#2ea3dc"/>
          <path d="M2 5l10 8 10-8M2 19l7-7M22 19l-7-7" fill="none" stroke="#ffffff" stroke-width="1.4"/>
        </svg>
        <span>daniel@merovanta.co.nz</span>
      </li>
    </ul>

    <div class="address">47 Harbour Lane Kelburn</div>

    <svg class="waves" viewBox="0 0 1200 894" aria-hidden="true">
      <path fill="#2e3f8b" d="M20 850 C 300 790 600 768 900 772 C 600 780 320 825 120 894 L 20 894 Z"/>
      <path fill="#2ea3dc" d="M130 894 C 360 822 700 772 1200 784 L 1200 894 Z"/>
    </svg>

    <div class="website">www.merovanta.co.nz</div>
  </div>
</body>
</html>
```